Visitenkarten-Design
Zielgruppe
Elektro und Automatisierungstechnik
Zielgruppe: Industriekunden
Aufgabenstellung
Zweiseitig farbig
Querformat 8,5*5,5cm
modernes, innovatives und zuverlässiges Unternehmen
Vorhandenes Logo muss integriert werden. Siehe Anhang

```html
<!DOCTYPE html>
<html lang="de">
<head>
<meta charset="utf-8">
<title>Visitenkarte Brettlinger Elektrotechnik</title>
<link href="https://fonts.googleapis.com/css2?family=Montserrat:wght@400;700&display=swap" rel="stylesheet">
<style>
  :root {
    --navy: #1b3a5c;
    --ink: #222222;
    --paper: #ffffff;
    --backdrop: #e2e2e2;
  }
  * { margin: 0; padding: 0; box-sizing: border-box; }
  html, body { width: 1200px; height: 1200px; overflow: hidden; }
  body {
    background: var(--backdrop);
    font-family: "Montserrat", Arial, sans-serif;
    position: relative;
  }
  .card {
    position: absolute;
    left: 322px;
    width: 556px;
    height: 360px;
    background: var(--paper);
  }
  .card--front { top: 180px; }
  .card--back { top: 600px; }

  .wordmark {
    position: absolute;
    display: flex;
    align-items: center;
    color: var(--navy);
    font-weight: 700;
    line-height: 1.05;
    text-transform: uppercase;
  }
  .wordmark__square {
    background: var(--navy);
    flex: none;
  }
  .card--front .wordmark {
    left: 128px; top: 112px; width: 300px; height: 116px;
    font-size: 30px; letter-spacing: 0.5px;
  }
  .card--front .wordmark__square { width: 26px; height: 26px; margin-right: 16px; }

  .card--back .wordmark {
    left: 303px; top: 42px; width: 220px; height: 85px;
    font-size: 20px; letter-spacing: 0.3px;
  }
  .card--back .wordmark__square { width: 18px; height: 18px; margin-right: 11px; }

  .person { position: absolute; left: 33px; top: 150px; }
  .person__name {
    color: var(--navy); font-weight: 700; font-size: 20px; letter-spacing: 0.2px;
  }
  .person__role {
    color: var(--ink); font-size: 13.5px; margin-top: 9px;
  }

  .contact {
    position: absolute; left: 303px; top: 193px;
    color: var(--ink); font-size: 13px; line-height: 18px; letter-spacing: 0.2px;
  }
  .contact__company { color: var(--navy); font-weight: 700; }
  .contact__gap { height: 18px; }
</style>
</head>
<body>
  <section class="card card--front">
    <div class="wordmark">
      <span class="wordmark__square"></span>
      <span>Brettlinger<br>Elektrotechnik</span>
    </div>
  </section>

  <section class="card card--back">
    <div class="wordmark">
      <span class="wordmark__square"></span>
      <span>Brettlinger<br>Elektrotechnik</span>
    </div>

    <div class="person">
      <p class="person__name">Jonas Brettlinger</p>
      <p class="person__role">Geschäftsführer</p>
    </div>

    <div class="contact">
      <p class="contact__company">Brettlinger Elektrotechnik GmbH</p>
      <p>Lindenweg 12</p>
      <p>87509 Hallerau</p>
      <div class="contact__gap"></div>
      <p>+49 98 765 43 21</p>
      <p>kontakt@brettlinger-elektro.de</p>
      <p>www.brettlinger-elektro.de</p>
    </div>
  </section>
</body>
</html>
```